Business Card Design Project

Please create a custom business card for Silverpine Golf Academy. The logo is attached to this brief.

Colours could be based on Blue, black, red, or white color. Colors like orange, green, purple, pink are not preferable.

Here is the link to the logo project : http://jobs.brieflantern.com/job.aspx?id=413057

Questions can be posted on the Discussion Board.

```html
<!DOCTYPE html>
<html lang="en">
<head>
<meta charset="utf-8">
<title>Silverpine Golf Academy – Business Card</title>
<link href="https://fonts.googleapis.com/css2?family=Open+Sans:wght@400;600;700&display=swap" rel="stylesheet">
<style>
  :root {
    --navy: #0b1f4d;
    --navy-soft: #22376a;
    --paper: #ffffff;
    --ground: #e4e2df;
    --ink-grey: #555a63;
    --mist: #eef0f4;
  }
  * { box-sizing: border-box; margin: 0; padding: 0; }
  html, body { width: 1200px; height: 997px; overflow: hidden; }
  body {
    background: var(--ground);
    font-family: "Open Sans", Arial, sans-serif;
    display: flex; align-items: center; justify-content: center; gap: 40px;
  }
  .card {
    position: relative; width: 550px; height: 314px; overflow: hidden;
    box-shadow: 0 6px 18px rgba(0,0,0,.12);
  }
  /* front face */
  .card-front { background: var(--navy); color: var(--paper); }
  .front-disc {
    position: absolute; width: 250px; height: 250px; border-radius: 50%;
    background: var(--navy-soft); left: 170px; top: 32px;
  }
  .front-brand {
    position: absolute; left: 0; right: 0; top: 132px; text-align: center;
  }
  .front-brand .brand-name { font-size: 30px; font-weight: 700; color: var(--paper); }
  .front-brand .brand-web { font-size: 13px; letter-spacing: 2px; margin-top: 4px; }
  /* back face */
  .card-back { background: var(--paper); color: var(--navy); }
  .back-disc {
    position: absolute; width: 300px; height: 300px; border-radius: 50%;
    background: var(--mist); right: -70px; top: -40px;
  }
  .back-brand {
    position: absolute; left: 32px; top: 118px; display: flex; align-items: center; gap: 10px;
  }
  .back-brand .brand-dot { width: 34px; height: 34px; border-radius: 50%; background: var(--navy); }
  .back-brand .brand-name { font-size: 24px; font-weight: 700; color: var(--navy); }
  .holder { position: absolute; right: 36px; top: 70px; text-align: right; }
  .holder-name { font-size: 17px; font-weight: 700; }
  .holder-role { font-size: 12px; color: var(--ink-grey); }
  .rule {
    position: absolute; left: 32px; right: 36px; top: 112px; height: 1.5px;
    background: linear-gradient(90deg, rgba(11,31,77,0), var(--navy));
  }
  .address { position: absolute; right: 36px; top: 128px; text-align: right; font-size: 12px; line-height: 1.5; color: var(--ink-grey); }
  .contacts { position: absolute; left: 32px; bottom: 28px; list-style: none; font-size: 13px; color: var(--ink-grey); }
  .contacts li { display: flex; align-items: center; gap: 8px; line-height: 21px; }
  .contacts svg { width: 13px; height: 13px; fill: var(--navy); }
</style>
</head>
<body>
  <section class="card card-front">
    <div class="front-disc"></div>
    <div class="front-brand">
      <div class="brand-name">Silverpine Golf Academy</div>
      <div class="brand-web">www.silverpinegolf.com</div>
    </div>
  </section>

  <section class="card card-back">
    <div class="back-disc"></div>
    <div class="holder">
      <div class="holder-name">Ethan Marlow</div>
      <div class="holder-role">Director</div>
    </div>
    <div class="rule"></div>
    <div class="address">Suite 40 Fairway Lane<br>Westfield, 2091, Canada</div>
    <div class="back-brand">
      <span class="brand-dot"></span>
      <span class="brand-name">Silverpine Golf Academy</span>
    </div>
    <ul class="contacts">
      <li><svg viewBox="0 0 16 16"><path d="M3 1h3l1 4-2 1c1 2 3 4 5 5l1-2 4 1v3c0 1-1 2-2 2C7 15 1 9 1 3c0-1 1-2 2-2z"/></svg>212 555 0148</li>
      <li><svg viewBox="0 0 16 16"><path d="M4 1h7v4H4zM2 6h12v7H2zm3 2v3h6V8z"/></svg>212 555 0193</li>
      <li><svg viewBox="0 0 16 16"><path d="M1 3h14v10H1zm1 1v1l6 4 6-4V4z"/></svg>hello@silverpinegolf.com</li>
      <li><svg viewBox="0 0 16 16"><path d="M8 1a7 7 0 100 14A7 7 0 008 1zm0 1.5c.8 0 1.8 1.8 2 4.5H6c.2-2.7 1.2-4.5 2-4.5zM2.6 7h2c.1-1.5.4-2.9 1-3.8A5.5 5.5 0 002.6 7zm8.8 0h2a5.5 5.5 0 00-3-3.8c.6.9.9 2.3 1 3.8zM2.6 9a5.5 5.5 0 003 3.8c-.6-.9-.9-2.3-1-3.8zm3.4 0c.2 2.7 1.2 4.5 2 4.5s1.8-1.8 2-4.5zm5.4 0c-.1 1.5-.4 2.9-1 3.8a5.5 5.5 0 003-3.8z"/></svg>www.silverpinegolf.com</li>
    </ul>
  </section>
</body>
</html>
```